New Architectural Firm Business Cards

New Business card to compliment previous pixel forum logo (attached). Please design a business card that is simple, modern, creative....please do not use "symbols", simply the logo and associated graphics/text. The front should contain name/address/phone/email/web address (with graphics).....back should be 100% graphic design using the logo somehow. Hoping for a two color (black and yellow) design. full bleed design, no borders

Target Market(s)

Commercial Architecture Clients

Industry/Entity Type

Architecture

Contact Information for Business Card

Please design a business card that is simple, modern, creative....please do not use "symbols", simply the logo and associated graphics/text. The front should contain name/address/phone/email/web address (with graphics).....back should be 100% graphic design using the logo somehow

Font styles to use
Sans Serif

Colors
FFF300
FFF600
FEFA6F
FFFEC7
FFFEE8

Requirements
Must have
• Clean, Modern Design
Should not have
• Stock images or "icons"

```html
<!DOCTYPE html>
<html lang="en">
<head>
<meta charset="utf-8">
<title>Pixel Forum – Business Card</title>
<link rel="stylesheet" href="https://fonts.googleapis.com/css2?family=Roboto:wght@400;700&display=swap">
<style>
  :root{
    --bg:#2b2b2b;
    --paper:#ffffff;
    --yellow:#f5c318;
    --yellow-light:#fbd55a;
    --ink:#1e1e1e;
    --white:#ffffff;
  }
  *{margin:0;padding:0;box-sizing:border-box}
  html,body{width:1200px;height:976px;overflow:hidden}
  body{
    background:var(--bg);
    font-family:"Roboto",Arial,sans-serif;
    display:flex;align-items:center;justify-content:center;gap:80px;
  }
  .card{
    width:400px;height:700px;position:relative;
    box-shadow:0 10px 30px rgba(0,0,0,.45);
  }
  .card--front{background:var(--paper);color:var(--ink)}
  .brand{
    position:absolute;top:150px;left:0;right:0;
    display:flex;align-items:center;justify-content:center;gap:14px;
  }
  .brand__mark{width:34px;height:34px;background:var(--yellow)}
  .brand__name{
    font-weight:700;font-size:40px;letter-spacing:2px;
    color:var(--yellow);text-transform:uppercase;
  }
  .contact{
    position:absolute;top:400px;left:0;right:0;text-align:center;
    font-size:17px;line-height:1.5;
  }
  .contact__name{
    font-weight:700;font-size:28px;letter-spacing:1px;
    color:var(--yellow);text-transform:uppercase;line-height:1.1;
  }
  .contact__role{font-size:17px;margin-top:2px}
  .contact__rule{width:22px;height:3px;background:var(--yellow);margin:14px auto}
  .card--back{
    background:linear-gradient(150deg,var(--yellow-light) 0%,var(--yellow) 55%,var(--yellow) 100%);
    overflow:hidden;
  }
  .card__pattern{position:absolute;inset:0}
  .back-brand{
    position:absolute;right:30px;bottom:36px;
    font-weight:700;font-size:22px;letter-spacing:1px;
    color:var(--white);text-transform:uppercase;
  }
</style>
</head>
<body>
  <section class="card card--front" aria-label="Card front">
    <div class="brand">
      <span class="brand__mark"></span>
      <span class="brand__name">Pixel Forum</span>
    </div>
    <div class="contact">
      <p class="contact__name">Dana Whitfield</p>
      <p class="contact__role">President</p>
      <div class="contact__rule"></div>
      <p>555 010 2040</p>
      <p>hello@pixelforum.studio</p>
      <p>www.pixelforum.studio</p>
      <div class="contact__rule"></div>
      <p>48 Harbor Ridge Avenue</p>
      <p>Suite 310, Lakeford</p>
    </div>
  </section>

  <section class="card card--back" aria-label="Card back">
    <div class="card__pattern" role="img" aria-label="Repeating brand pattern in light yellow tones across the card"></div>
    <p class="back-brand">Pixel Forum</p>
  </section>
</body>
</html>
```